Website Design for Car Donations

Revise current site www.wheelsforheroes-sample.org

Sites i like:

https://www.autogiftbrigade.example

https://ridegivingcorps.example

https://protoboardly.example/7a2d91e4/screen/58217046

```html
<!DOCTYPE html>
<html lang="en">
<head>
<meta charset="utf-8">
<title>Wheels for Heroes — Donate Your Car</title>
<link href="https://fonts.googleapis.com/css2?family=Open+Sans:wght@300;400;600;700;800&display=swap" rel="stylesheet">
<style>
:root{
  --red:#c40d0d;
  --red-dark:#a30808;
  --yellow:#fec60a;
  --yellow-deep:#f5b800;
  --ink:#222;
  --dark:#2b2b2b;
  --darker:#1f1f1f;
  --grey-bg:#f4f4f4;
  --panel:#f0f0f0;
  --muted:#666;
  --white:#fff;
}
*{box-sizing:border-box;margin:0;padding:0}
html,body{width:1200px;height:3103px;overflow:hidden}
body{position:relative;font-family:"Open Sans",Arial,sans-serif;color:var(--ink);background:var(--white)}
.abs{position:absolute}

/* top bar */
.topbar{top:0;left:0;width:1200px;height:31px;background:var(--red)}
.topbar .call{right:0;top:0;width:500px;height:31px;background:var(--yellow);display:flex;align-items:center;padding-left:60px;font-size:11px;color:#6a4b00;letter-spacing:.3px}
.topbar .call b{font-style:italic;color:var(--ink);margin-left:4px}
.topbar .call .dot{position:absolute;left:16px;top:4px;width:23px;height:23px;border-radius:50%;background:var(--red)}
.search{left:250px;top:6px;width:125px;height:19px;border-bottom:1px solid rgba(255,255,255,.4);color:#fff;font-size:11px}
.social-top{left:380px;top:0;display:flex}
.social-top span{width:41px;height:31px;border-left:1px solid rgba(255,255,255,.2);display:flex;align-items:center;justify-content:center}
.social-top span i{width:9px;height:9px;border-radius:50%;background:#fff;display:block}

/* header */
.header{top:31px;left:0;width:1200px;height:92px;background:#fff}
.brand{left:252px;top:28px;display:flex;align-items:center;gap:8px;font-weight:800;font-size:19px;color:var(--red)}
.brand .mark{width:16px;height:16px;border-radius:50%;background:var(--yellow)}
.nav{left:534px;top:38px;display:flex;gap:20px;font-size:10px;font-weight:600;color:#333}
.donate-tab{left:918px;top:31px;width:32px;height:110px;background:var(--yellow);border-radius:0 0 16px 16px;writing-mode:vertical-rl;font-size:9px;font-weight:700;display:flex;align-items:center;justify-content:center}

/* hero */
.hero{top:123px;left:0;width:1200px;height:520px;background:linear-gradient(100deg,#6a6a55 0%,#b9aa92 30%,#dfe7ef 55%,#c6d8e8 100%)}
.form{left:604px;top:196px;width:346px;height:400px;background:var(--dark);padding:0 22px}
.form .car-badge{position:absolute;left:148px;top:-25px;width:50px;height:50px;border-radius:50%;background:var(--yellow)}
.form h2{margin:0 -22px;height:40px;background:var(--yellow);font-size:19px;font-weight:800;text-align:center;line-height:44px}
.form .sub{color:#fff;text-align:center;font-size:14px;margin:14px 0 12px}
.field{background:#fff;height:33px;font-size:10px;color:#555;padding:11px 10px;margin-bottom:14px;position:relative}
.row{display:flex;gap:10px}.row .field{flex:1}
.field.sel::after{content:"";position:absolute;right:10px;top:14px;border:4px solid transparent;border-top-color:#333}
.btn{height:36px;background:var(--yellow);text-align:center;font-size:11px;font-weight:700;line-height:36px;margin-top:2px;border-bottom:3px solid var(--yellow-deep)}

/* benefits */
.benefits-bg{top:560px;left:0;width:1200px;height:540px}
.benefits-title{top:722px;left:0;width:1200px;text-align:center;color:#fff}
.benefits-title .l1{font-size:29px;font-weight:300}
.benefits-title .l2{font-size:29px;font-weight:700}
.benefits{top:835px;left:100px;width:1000px;display:flex;justify-content:space-between}
.benefit{width:140px;text-align:center;color:#fff;font-size:12px;line-height:1.3}
.benefit .ic{width:70px;height:70px;border-radius:50%;background:#fff;margin:0 auto 16px;display:flex;align-items:center;justify-content:center}
.benefit b{display:block;font-weight:700}

/* how */
.how{top:1100px;left:0;width:1200px;height:400px;background:var(--grey-bg)}
.h-sec{font-size:29px;font-weight:800;color:var(--red);text-align:center}
.steps{top:1225px;left:230px;width:740px;display:flex;justify-content:space-between}
.step{width:230px;text-align:center}
.step .illu{width:150px;height:115px;margin:0 auto 30px;border-radius:8px}
.step h3{font-size:12px;font-weight:700;margin-bottom:8px;line-height:1.35}
.step p{font-size:10px;color:var(--muted);line-height:1.55}

/* why */
.why{top:1500px;left:0;width:1200px;height:520px;background:var(--yellow)}
.why-photo{top:1505px;left:550px;width:650px;height:510px;background:radial-gradient(circle at 55% 50%,#6fa2c4 0%,#9fb7a8 22%,#e9c2b0 40%,#f6e6e4 70%,#fff 100%);clip-path:polygon(0 0,100% 0,100% 100%,14% 100%)}
.why h2{position:absolute;left:120px;top:60px;font-size:29px;font-weight:800;line-height:1.1}
.why ul{position:absolute;left:120px;top:150px;width:440px;list-style:none}
.why li{position:relative;padding-left:24px;font-size:10.5px;line-height:1.6;margin-bottom:21px}
.why li::before{content:"";position:absolute;left:0;top:3px;width:13px;height:13px;border-radius:50%;background:var(--ink)}
.why li::after{content:"";position:absolute;left:3px;top:7px;border:3px solid transparent;border-left:5px solid var(--yellow)}

/* faq */
.faq-title{top:2070px;left:0;width:1200px}
.faq-col{top:2150px;width:475px}
.q{height:48px;background:var(--panel);font-size:12.5px;color:#444;padding:0 22px;display:flex;align-items:center;justify-content:space-between;margin-bottom:18px}
.q .pm{width:26px;height:26px;border-radius:50%;background:#fff;font-size:18px;line-height:26px;text-align:center;color:#333}
.q.open{background:var(--red);color:#fff;margin-bottom:0}
.q.open .pm{color:var(--red)}
.answer{background:var(--red-dark);color:#fff;font-size:9px;line-height:1.6;padding:14px 22px;margin-bottom:18px}

/* about */
.about{top:2462px;left:0;width:1200px;height:205px;background:var(--yellow);text-align:center}
.about h2{margin-top:42px;font-size:27px;font-weight:800;color:var(--red)}
.about p{width:700px;margin:14px auto 0;font-size:14px;line-height:1.7;color:#7a5a00}

/* footer */
.footer{top:2667px;left:0;width:1200px;height:380px;background:var(--dark);text-align:center;color:#fff}
.footer .brand{position:static;justify-content:center;margin-top:52px;font-size:21px;color:#fff}
.footer nav{margin-top:42px;display:flex;justify-content:center;gap:22px;font-size:11px;font-weight:600}
.footer .call{margin-top:38px;font-size:16px;font-style:italic}
.footer .call b{color:var(--yellow);font-weight:700}
.footer .ops{font-size:11px;margin-top:4px}
.badges{margin-top:22px;display:flex;justify-content:center;gap:28px}
.badges span{width:60px;height:28px;border-radius:4px;background:#555}
.badges span.round{width:38px;height:38px;border-radius:50%;background:#6a8fa6;margin-top:-5px}
.soc{margin-top:22px;display:flex;justify-content:center;gap:6px}
.soc span{width:22px;height:22px;border-radius:50%;background:#fff}
.soc span.hl{background:var(--yellow)}
.copy{top:3047px;left:0;width:1200px;height:56px;background:var(--darker);color:#ddd;font-size:10px;text-align:center;padding-top:18px}
.copy a{color:var(--yellow);text-decoration:none;font-weight:700}
</style>
</head>
<body>

<div class="abs topbar">
  <div class="abs search">Search...</div>
  <div class="abs social-top"><span><i></i></span><span><i></i></span><span><i></i></span><span><i></i></span><span><i></i></span><span><i></i></span></div>
  <div class="abs call"><span class="dot"></span>CALL TODAY TO DONATE : <b>1-800-555-0142</b></div>
</div>

<header class="abs header">
  <div class="abs brand"><span class="mark"></span>WHEELS FOR HEROES</div>
  <nav class="abs nav"><span>HOME</span><span>ABOUT</span><span>HOW TO DONATE</span><span>WHY DONATE</span><span>FAQ</span><span>CONTACT US</span></nav>
</header>
<div class="abs donate-tab">DONATE NOW!</div>

<div class="abs hero" role="img" aria-label="Photo of a uniformed service member holding a small flag, embracing a child, against a bright sky"></div>

<svg class="abs benefits-bg" width="1200" height="540" viewBox="0 0 1200 540">
  <polygon points="0,20 420,145 1200,30 1200,540 0,540" fill="#c40d0d"/>
  <polygon points="330,118 420,145 510,132 420,178" fill="#fec60a"/>
  <polygon points="0,450 720,510 1200,450 1200,540 0,540" fill="#f4f4f4"/>
  <polygon points="560,500 720,510 920,478 720,530" fill="#fec60a"/>
</svg>

<form class="abs form">
  <span class="car-badge"></span>
  <h2>DONATE YOUR CAR ONLINE</h2>
  <p class="sub">FULL TAX DEDUCTION - RUNNING OR NOT</p>
  <div class="row"><div class="field">First Name</div><div class="field">Last Name</div></div>
  <div class="row"><div class="field">Daytime Phone</div><div class="field">Email</div></div>
  <div class="row"><div class="field">Zip Code</div><div class="field sel">Choose Year</div></div>
  <div class="field sel">Choose Make</div>
  <div class="field">Vehicle Model</div>
  <div class="btn">DONATE NOW</div>
</form>

<div class="abs benefits-title"><div class="l1">DONATE YOUR CAR TO VETERANS</div><div class="l2">MAKE A DIFFERENCE</div></div>
<div class="abs benefits">
  <div class="benefit"><div class="ic"><svg width="34" height="34" viewBox="0 0 34 34"><circle cx="17" cy="17" r="14" fill="none" stroke="#222" stroke-width="2.5"/><path d="M10 17l5 5 9-10" fill="none" stroke="#222" stroke-width="2.5"/></svg></div>YOU HAVE<b>NO COSTS</b></div>
  <div class="benefit"><div class="ic"><svg width="34" height="34" viewBox="0 0 34 34"><rect x="4" y="12" width="18" height="10" fill="#222"/><path d="M22 14h5l3 5v3h-8z" fill="#222"/><circle cx="10" cy="25" r="3" fill="#222"/><circle cx="25" cy="25" r="3" fill="#222"/></svg></div>FREE TOWING<b>RUNNING OR NOT</b></div>
  <div class="benefit"><div class="ic"><svg width="34" height="34" viewBox="0 0 34 34"><rect x="8" y="4" width="18" height="26" fill="none" stroke="#222" stroke-width="2.5"/><path d="M12 11h10M12 16h10M12 21h6" stroke="#222" stroke-width="2"/></svg></div>WE ISSUE YOU AN<b>IRS TAX RECEIPT</b></div>
  <div class="benefit"><div class="ic"><svg width="34" height="34" viewBox="0 0 34 34"><rect x="6" y="4" width="18" height="24" fill="none" stroke="#222" stroke-width="2.5"/><circle cx="20" cy="19" r="6" fill="#fff" stroke="#222" stroke-width="2.5"/><path d="M24 23l6 6" stroke="#222" stroke-width="3"/></svg></div>WE TAKE CARE OF<b>ALL PAPERWORK</b></div>
  <div class="benefit"><div class="ic"><svg width="34" height="34" viewBox="0 0 34 34"><rect x="8" y="6" width="18" height="24" fill="none" stroke="#222" stroke-width="2.5"/><rect x="13" y="3" width="8" height="5" fill="#222"/><path d="M12 15h10M12 20h10M12 25h6" stroke="#222" stroke-width="2"/></svg></div>NO DMV<b>HASSLES</b></div>
  <div class="benefit"><div class="ic"><svg width="34" height="34" viewBox="0 0 34 34"><rect x="6" y="10" width="22" height="18" rx="2" fill="#222"/><rect x="13" y="5" width="8" height="6" fill="none" stroke="#222" stroke-width="2.5"/></svg></div>VACATION<b>VOUCHER</b></div>
</div>

<section class="abs how">
  <h2 class="h-sec" style="margin-top:52px">HOW TO DONATE</h2>
</section>
<div class="abs steps">
  <div class="step"><div class="illu" role="img" aria-label="Illustration of a hand filling out an online form on a screen" style="background:linear-gradient(180deg,#fde9a6,#f6d3c0)"></div><h3>CALL US AT 1-800-555-0142 OR<br>FILL OUT THE ONLINE FORM</h3><p>Donating your vehicle is easy and donation<br>is accepted nationwide.</p></div>
  <div class="step"><div class="illu" role="img" aria-label="Illustration of a yellow tow truck" style="background:linear-gradient(180deg,#fcd65a,#b9b9b9)"></div><h3>WE TOW THE VEHICLE</h3><p>Any vehicles are accepted and we will arrange to pick up your vehicle when it is most convenient for you.</p></div>
  <div class="step"><div class="illu" role="img" aria-label="Illustration of a paper receipt scroll and pencil" style="background:linear-gradient(180deg,#dfe6ee,#f3c9c4)"></div><h3>TAX WRITE-OFF</h3><p>Once the vehicle donation is complete, you will receive your tax deductable vehicle donation receipt.</p></div>
</div>

<section class="abs why">
  <h2>WHY DONATE YOUR<br>CAR TO US</h2>
  <ul>
    <li>IRS 501(c)3 Approved : Free 24/7 Pickup with No DMV Hassles.</li>
    <li>Free Local Towing : We will pick up your car donation, running or not, when it's most convenient, at home or work.</li>
    <li>Income Tax Deduction : We issue you an IRS tax receipt and get you the highest tax write-off possible.</li>
    <li>No Paperwork Hassles : We handle everything: DMV and IRS paperwork.</li>
    <li>Car donations help fund programs : And benefit Valor Path Foundation. An IRS 501(c)3 nonprofit organization.</li>
    <li>Schedule a Free Pickup : Complete the form and a representative will call you to arrange a convenient time to pickup your car.</li>
  </ul>
</section>
<div class="abs why-photo" role="img" aria-label="Photo of cupped hands holding up a globe"></div>

<h2 class="abs h-sec faq-title">FREQUENTLY ASKED QUESTIONS</h2>
<div class="abs faq-col" style="left:120px">
  <div class="q">What types of vehicles can be donated?<span class="pm">+</span></div>
  <div class="q open">Is my donated vehicle tax-deductible?<span class="pm">−</span></div>
  <div class="answer">Yes, we are a 501(c)(3) organization approved by the IRS to receive donated items and issue a tax-deductible donation receipt for the item. Your vehicle donation may be fully tax deductible based on your personal tax situation. Please check with your tax advisor.</div>
  <div class="q">When will I receive my tax receipt?<span class="pm">+</span></div>
</div>
<div class="abs faq-col" style="left:605px">
  <div class="q">What paperwork do I need to donate my vehicle?<span class="pm">+</span></div>
  <div class="q">What if the vehicle is not registered in my name?<span class="pm">+</span></div>
  <div class="q">How much will I receive as a tax deduction for my vehicle?<span class="pm">+</span></div>
  <div class="q">How do I schedule a pick up?<span class="pm">+</span></div>
</div>

<section class="abs about">
  <h2>ABOUT WHEELS FOR HEROES</h2>
  <p>Car donations help fund programs and benefit Valor Path Foundation. An IRS 501(c)3 nonprofit organization. Schedule a Free Pickup: Complete the form and a representative will call you to arrange a convenient time to pickup your car</p>
</section>

<footer class="abs footer">
  <div class="brand"><span class="mark" style="background:var(--red)"></span>WHEELS FOR HEROES</div>
  <nav><span>HOME</span><span>ABOUT</span><span>HOW TO DONATE</span><span>WHY DONATE</span><span>FAQ</span><span>CONTACT US</span></nav>
  <div class="call">CALL TODAY TO DONATE &nbsp;<b>1-800-555-0142</b></div>
  <div class="ops">Live Operators Available - 7 Days A Week</div>
  <div class="badges"><span></span><span class="round"></span></div>
  <div class="soc"><span></span><span></span><span class="hl"></span><span></span><span></span><span></span></div>
</footer>
<div class="abs copy">Copyright © 2017 <b>WHEELS FOR HEROES</b>. <a>PRIVACY POLICY</a>. All Rights Reserved.</div>

</body>
</html>
```